A modern web page for a software product

We need a web page for a software product, which is an advanced solution based on Machine Learning and Natural Language processing. We already have a logo of the product and expect the web page to be inline with the logo colors. The design should be for one page web site with scrolled sections - details of the content and guidelines in the attachments.

Target Market(s)

software company

Industry/Entity Type

It Company

Number of Pages Required

1 page

Colors

Designer to choose colors to be used in the design.

Requirements
Must have
• - modern icons and graphics
• - inline with the logo colors
• - be related to Machine Learining, AI, data processing
• - should have two language versions: english and polish both are attached.
Nice to have
• - animation/motion
Should not have
• - any photos embedded

```html
<!DOCTYPE html>
<html lang="en">
<head>
<meta charset="utf-8">
<title>Dataveil for GDPR</title>
<link rel="stylesheet" href="https://fonts.googleapis.com/css2?family=Open+Sans:wght@400;600;700&family=Playfair+Display:ital,wght@0,700;1,700&display=swap">
<style>
:root{
  --teal:#1fb5b0;
  --teal-dark:#14908c;
  --navy:#1b2836;
  --navy-2:#243446;
  --slate:#3a4b5e;
  --ink:#333c46;
  --muted:#7a838c;
  --line:#d5dadf;
  --white:#ffffff;
  --footer:#2b2f33;
}
*{margin:0;padding:0;box-sizing:border-box}
html,body{width:1200px;height:3656px;overflow:hidden}
body{font-family:"Open Sans",Arial,sans-serif;color:var(--ink);background:var(--white);position:relative}
section,header,footer{position:absolute;left:0;width:1200px}
.abs{position:absolute}
.brand{font-family:"Open Sans",Arial,sans-serif;font-weight:700;color:var(--teal);font-size:30px;display:flex;align-items:center;gap:10px}
.brand .mark{width:22px;height:22px;background:var(--teal)}
.section-title{position:absolute;font-family:"Playfair Display",Georgia,serif;font-weight:700;font-style:italic;font-size:22px;display:flex;align-items:center;gap:14px}
.section-title::before{content:"";width:60px;height:3px;background:var(--teal)}

/* hero */
.hero{top:0;height:740px;background:linear-gradient(160deg,#3d4c5c 0%,#26323f 55%,#1d2631 100%);color:var(--white)}
.hero-bg{position:absolute;inset:0}
.nav{position:absolute;top:22px;left:300px;display:flex;gap:30px;font-size:14px;font-weight:600}
.social{position:absolute;top:20px;right:40px;display:flex;gap:14px}
.social span{width:24px;height:24px;border-radius:50%;background:var(--white)}
.hero-title{position:absolute;top:118px;left:0;width:1200px;text-align:center;font-size:28px;font-weight:600;letter-spacing:.5px}
.hex-text{font-family:"Open Sans",Arial,sans-serif;font-weight:700;font-size:15px;fill:var(--white)}
.btn{position:absolute;top:646px;height:36px;width:140px;font-size:13px;font-weight:700;display:flex;align-items:center;justify-content:center;border-radius:3px}
.btn-primary{left:440px;background:var(--teal);color:var(--white)}
.btn-ghost{left:620px;border:2px solid var(--white);color:var(--white)}

/* features */
.features{top:740px;height:740px;background:var(--white)}
.lead{position:absolute;left:300px;top:152px;width:620px;border-top:1px solid var(--line);padding-top:14px}
.lead h3{color:var(--teal);font-size:17px;font-weight:600;margin-bottom:10px}
.lead ul{list-style:none;font-size:14px;line-height:24px;color:var(--muted)}
.lead li::before{content:"• ";color:var(--teal)}
.lead .sub{padding-left:18px}
.feature{position:absolute;display:flex;gap:18px;align-items:center;width:320px;font-size:15px;line-height:21px}
.feature svg{flex:none}

/* use cases */
.usecases{top:1480px;height:700px;background:linear-gradient(120deg,#2a3947 0%,#3b4c5d 45%,#233040 100%);color:var(--white)}
.usecases .section-title{color:var(--white)}
.case{position:absolute;display:flex;gap:20px;align-items:flex-start;font-size:15px;line-height:22px;width:440px}
.case ul{list-style:none;margin-top:6px}
.case li::before{content:"• "}

/* apart */
.apart{top:2180px;height:692px;background:linear-gradient(135deg,#34495c 0%,#4d6579 50%,#2d3e4f 100%);color:var(--white)}
.apart .section-title{color:var(--white)}
.point{position:absolute;left:120px;width:680px;display:flex;gap:14px;font-size:14px;line-height:21px}
.point b{font-weight:600;display:block}
.point ul{list-style:none;padding-left:20px}

/* contact */
.contact{top:2872px;height:488px;background:var(--white)}
.contact h2{position:absolute;font-size:26px;font-weight:400;color:var(--ink)}
.field{position:absolute;left:200px;width:220px;height:24px;border:1px solid var(--line);font-size:11px;color:#aaa;padding:4px 6px}
.label{position:absolute;font-size:11px;color:var(--muted)}
.send{position:absolute;left:220px;top:436px;width:60px;height:26px;background:var(--teal);color:var(--white);font-size:12px;font-weight:700;display:flex;align-items:center;justify-content:center}
.subscribe-input{position:absolute;left:700px;top:208px;width:190px;height:32px;border:1px solid var(--line);font-size:12px;color:#aaa;padding:8px 10px}
.subscribe-btn{position:absolute;left:900px;top:208px;width:92px;height:32px;border:2px solid var(--teal);color:var(--teal);font-size:12px;font-weight:700;display:flex;align-items:center;justify-content:center}

/* footer */
.footer{top:3360px;height:296px;background:var(--footer);color:#cfd4d8}
.footer-nav{position:absolute;top:38px;left:0;width:1200px;display:flex;justify-content:center;gap:30px;font-size:13px}
.footer-contact{position:absolute;left:880px;top:24px;font-size:12px;line-height:18px}
.footer-contact div{display:flex;gap:10px;align-items:flex-start;margin-bottom:14px}
.map{position:absolute;left:860px;top:140px;width:300px;height:120px;background:linear-gradient(135deg,#d9dfd2,#c7d0c9)}
.copy{position:absolute;bottom:10px;width:1200px;text-align:center;font-size:11px;color:#8b9197}
</style>
</head>
<body>

<header class="hero">
  <div class="hero-bg" role="img" aria-label="Dark background image of data and machine learning visuals"></div>
  <div class="brand abs" style="left:30px;top:14px"><span class="mark"></span>Lexora</div>
  <nav class="nav"><span>Home</span><span>Products</span><span>Support</span><span>Case Studies</span><span>About Us</span><span>Contact Us</span></nav>
  <div class="social"><span></span><span></span><span></span></div>
  <svg class="abs" style="left:0;top:0" width="1200" height="740" viewBox="0 0 1200 740">
    <g stroke="#ffffff" stroke-width="2" fill="none" opacity=".8">
      <line x1="280" y1="292" x2="610" y2="284"/>
      <line x1="220" y1="394" x2="410" y2="490"/>
      <line x1="530" y1="490" x2="670" y2="384"/>
      <line x1="790" y1="384" x2="990" y2="500"/>
    </g>
    <g fill="#1c3a5e" fill-opacity=".85" stroke="#ffffff" stroke-width="3">
      <polygon points="40,292 100,188 220,188 280,292 220,396 100,396"/>
      <polygon points="610,284 670,180 790,180 850,284 790,388 670,388"/>
      <polygon points="350,490 410,386 530,386 590,490 530,594 410,594"/>
      <polygon points="930,500 990,396 1110,396 1170,500 1110,604 990,604"/>
    </g>
    <g class="hex-text" text-anchor="middle">
      <text x="160" y="286">Discovery &amp; Classification</text><text x="160" y="308">of Personal Data</text>
      <text x="730" y="278">Unified Registry of All</text><text x="730" y="300">Personal Data</text>
      <text x="470" y="484">Consents Management</text><text x="470" y="506">Support</text>
      <text x="1050" y="494">Supports Structured &amp;</text><text x="1050" y="516">Unstructured Data Sources</text>
    </g>
  </svg>
  <h1 class="hero-title">Dataveil for GDPR</h1>
  <a class="btn btn-primary">GET STARTED</a>
  <a class="btn btn-ghost">LEARN MORE</a>
</header>

<section class="features">
  <h2 class="section-title" style="left:400px;top:62px">Main Features</h2>
  <div class="lead">
    <h3>Detection of personal and sensitive data for GDPR compliance</h3>
    <ul>
      <li>in structured sources (e.g. SQL servers)</li>
      <li>in unstructured sources</li>
      <li class="sub">(e.g. documents, e-mails, logs, data streams)</li>
      <li>in "noisy" content written in natural language</li>
      <li class="sub">(e.g. containing errors or custom formats)</li>
      <li>built-in ML models and rules for personal data used in Poland</li>
    </ul>
  </div>
  <div class="feature" style="left:32px;top:430px">
    <svg width="70" height="50" viewBox="0 0 70 50"><g fill="#333c46"><circle cx="35" cy="10" r="7"/><circle cx="10" cy="40" r="7"/><circle cx="35" cy="40" r="7"/><circle cx="60" cy="40" r="7"/></g><path d="M35 17v16M35 25H10v8M35 25h25v8" stroke="#1fb5b0" stroke-width="3" fill="none"/></svg>
    <span>Fast cataloging and classification of data set</span>
  </div>
  <div class="feature" style="left:440px;top:424px">
    <svg width="60" height="60" viewBox="0 0 60 60"><circle cx="30" cy="30" r="10" fill="#1fb5b0"/><g stroke="#333c46" stroke-width="3"><line x1="30" y1="4" x2="30" y2="18"/><line x1="30" y1="42" x2="30" y2="56"/><line x1="4" y1="30" x2="18" y2="30"/><line x1="42" y1="30" x2="56" y2="30"/></g><g fill="#333c46"><circle cx="30" cy="4" r="4"/><circle cx="30" cy="56" r="4"/><circle cx="4" cy="30" r="4"/><circle cx="56" cy="30" r="4"/></g></svg>
    <span>Unified data registry for RODO compliance</span>
  </div>
  <div class="feature" style="left:872px;top:424px">
    <svg width="70" height="60" viewBox="0 0 70 60"><g fill="#333c46"><circle cx="35" cy="10" r="8"/><rect x="4" y="40" width="16" height="16"/><rect x="27" y="40" width="16" height="16"/><rect x="50" y="40" width="16" height="16"/></g><path d="M35 18v12M12 40V30h46v10M35 30v10" stroke="#1fb5b0" stroke-width="3" fill="none"/></svg>
    <span>Management of consents and data access policies</span>
  </div>
  <div class="feature" style="left:32px;top:584px">
    <svg width="60" height="60" viewBox="0 0 60 60"><rect x="4" y="6" width="52" height="40" fill="none" stroke="#333c46" stroke-width="3"/><rect x="12" y="28" width="7" height="12" fill="#1fb5b0"/><rect x="24" y="20" width="7" height="20" fill="#1fb5b0"/><rect x="36" y="14" width="7" height="26" fill="#333c46"/><rect x="20" y="48" width="20" height="4" fill="#333c46"/></svg>
    <span>Customizable analytics and reporting</span>
  </div>
  <div class="feature" style="left:440px;top:580px">
    <svg width="64" height="64" viewBox="0 0 64 64"><circle cx="32" cy="32" r="24" fill="none" stroke="#333c46" stroke-width="12"/><path d="M32 8a24 24 0 0 1 24 24" fill="none" stroke="#1fb5b0" stroke-width="12"/></svg>
    <span>Ability to integrates with tools for data anonymization or depersonalization</span>
  </div>
  <div class="feature" style="left:872px;top:584px">
    <svg width="60" height="60" viewBox="0 0 60 60"><circle cx="26" cy="28" r="16" fill="none" stroke="#333c46" stroke-width="8" stroke-dasharray="6 4"/><circle cx="26" cy="28" r="6" fill="#1fb5b0"/><circle cx="48" cy="48" r="8" fill="#1fb5b0"/></svg>
    <span>RESTful API for system management and integration</span>
  </div>
</section>

<section class="usecases">
  <div class="abs" style="inset:0" role="img" aria-label="Dark background image of people working at computers"></div>
  <h2 class="section-title" style="left:0;top:36px">Use cases</h2>
  <div class="case" style="left:40px;top:120px">
    <svg width="60" height="60" viewBox="0 0 60 60"><circle cx="24" cy="24" r="16" fill="none" stroke="#fff" stroke-width="4"/><line x1="36" y1="36" x2="54" y2="54" stroke="#fff" stroke-width="6"/><path d="M14 26l6-8 6 6 8-10" stroke="#1fb5b0" stroke-width="3" fill="none"/></svg>
    <span>Internal audits and verification of the current status - in preparation for meeting RODO compliance RODO</span>
  </div>
  <div class="case" style="left:660px;top:130px">
    <svg width="60" height="54" viewBox="0 0 60 54"><circle cx="30" cy="10" r="9" fill="#fff"/><g fill="#fff"><circle cx="8" cy="44" r="8"/><circle cx="30" cy="44" r="8"/><circle cx="52" cy="44" r="8"/></g><path d="M30 19v17M30 28H8v8M30 28h22v8" stroke="#fff" stroke-width="3" fill="none"/></svg>
    <span>Cataloging sources that store sensitive data</span>
  </div>
  <div class="case" style="left:40px;top:268px">
    <svg width="60" height="60" viewBox="0 0 60 60"><rect x="8" y="4" width="36" height="46" fill="none" stroke="#fff" stroke-width="3"/><line x1="15" y1="16" x2="37" y2="16" stroke="#fff" stroke-width="3"/><line x1="15" y1="26" x2="37" y2="26" stroke="#fff" stroke-width="3"/><ellipse cx="42" cy="46" rx="14" ry="8" fill="#1fb5b0"/><circle cx="42" cy="46" r="4" fill="#fff"/></svg>
    <span>Keeping the registry of personal data in order to implement rights to information, forgetfulness, data transfer</span>
  </div>
  <div class="case" style="left:660px;top:300px">
    <svg width="60" height="60" viewBox="0 0 60 60"><circle cx="30" cy="30" r="24" fill="#fff"/><path d="M30 30V6a24 24 0 0 1 24 24z" fill="#1fb5b0"/><circle cx="30" cy="30" r="10" fill="#2f3e4e"/></svg>
    <span>Continuous monitoring and classification of data</span>
  </div>
  <div class="case" style="left:340px;top:430px;width:520px">
    <svg width="70" height="60" viewBox="0 0 70 60"><rect x="6" y="36" width="10" height="20" fill="#fff"/><rect x="22" y="28" width="10" height="28" fill="#fff"/><rect x="38" y="20" width="10" height="36" fill="#fff"/><path d="M6 26L28 12l14 8L64 4" stroke="#1fb5b0" stroke-width="4" fill="none"/></svg>
    <div>Use collected the data to create additional business value, e.g.:
      <ul><li>classification of documents</li><li>analysis of sentiment</li><li>customer analytics for marketing</li><li>fraud detection</li><li>data governance</li></ul>
    </div>
  </div>
</section>

<section class="apart">
  <div class="abs" style="inset:0" role="img" aria-label="Background of connected network nodes"></div>
  <h2 class="section-title" style="left:0;top:6px">What sets us apart</h2>
  <div class="point" style="top:60px"><span>✔</span><div><b>Built-in support for detection of Polish personal data</b>
    <ul><li>sensitive data (e.g. PESEL, NIP, ID card, etc.)</li><li>content of documents</li><li>metadata describing the data (ownership, system, table, author, etc.)</li><li>metadata describing the detection process</li></ul></div></div>
  <div class="point" style="top:204px"><span>✔</span><div><b>High effectiveness of personal data detection (also "noisy" data) by combining:</b>
    <ul><li>Natural Language Processing</li><li>Machine Learning</li><li>expert rules</li><li>custom models for data detection specific to your organization needs</li></ul></div></div>
  <div class="point" style="top:348px"><span>✔</span><div><b>Supports structured and unstructured data sources</b>
    <ul><li>multiple systems, mail servers, content management, data servers, web server, etc.</li><li>multiple formats: texts, images, archives, mails, etc.</li><li>relational databases</li><li>NoSQL databases</li><li>data streams</li></ul></div></div>
  <div class="point" style="top:506px"><span>✔</span><div><b>Ready for high performance processing</b>
    <ul><li>handles TBs of data easily</li><li>linear scalability</li><li>high availability and fault tolerance</li></ul></div></div>
</section>

<section class="contact">
  <h2 style="left:248px;top:36px">Contact Us</h2>
  <div class="field" style="top:90px">Name</div>
  <div class="field" style="top:122px">Phone</div>
  <div class="field" style="top:154px">Email</div>
  <div class="field" style="top:186px;width:320px;height:96px">Enter Message</div>
  <div class="label" style="left:200px;top:296px">Type the characters you see in the picture</div>
  <div class="abs" style="left:200px;top:316px;width:130px;height:34px;background:linear-gradient(90deg,#d8dde2,#eef0f2)" role="img" aria-label="Verification code image"></div>
  <div class="label" style="left:200px;top:392px">characters</div>
  <div class="field" style="left:260px;top:388px;width:160px"></div>
  <div class="send">Send</div>
  <h2 style="left:690px;top:166px;font-size:22px">Subscribe to Our Newsletter</h2>
  <div class="subscribe-input">Email Address</div>
  <div class="subscribe-btn">SIGN UP</div>
</section>

<footer class="footer">
  <nav class="footer-nav"><span>Home</span><span>Products</span><span>Support</span><span>Awards</span><span>Blog</span><span>About Us</span><span>Contact Us</span></nav>
  <div class="footer-contact">
    <div><svg width="14" height="18" viewBox="0 0 14 18"><path d="M7 0a7 7 0 0 1 7 7c0 5-7 11-7 11S0 12 0 7a7 7 0 0 1 7-7z" fill="#cfd4d8"/><circle cx="7" cy="7" r="2.5" fill="#2b2f33"/></svg><span>12 Orchard Lane<br>00-101 Northfield</span></div>
    <div><svg width="14" height="14" viewBox="0 0 14 14"><path d="M3 0l3 3-2 2a9 9 0 0 0 5 5l2-2 3 3-2 3C6 14 0 8 0 3z" fill="#cfd4d8"/></svg><span>(000) 555-0142</span></div>
    <div><svg width="14" height="12" viewBox="0 0 14 12"><rect width="14" height="12" fill="#cfd4d8"/><path d="M0 0l7 6 7-6" stroke="#2b2f33" fill="none"/></svg><span>info@lexora.example</span></div>
  </div>
  <div class="map" role="img" aria-label="Map showing the office location"></div>
  <div class="brand abs" style="left:30px;top:150px;font-size:40px"><span class="mark" style="width:30px;height:30px"></span>Lexora</div>
  <div class="copy">© 2024 Dataveil. All rights reserved.</div>
</footer>

</body>
</html>
```